" A MOURALVES E TEIXEDO SOCIEDADE DE ADVOGADOS é a concretização de um ideal instituído nos idos de 2007, tempo em que os sócios fundadores ainda ocupavam os bancos da Faculdade de Direito. Sediada no Jardim Jardim Vila Serena na cidade de Sorocaba, seu Escritório conta com modernas instalações e com uma equipe selecionada de Advogados e Colaboradores especializados. Atualmente, em decorrência de sua organização operacional e do comprometimento ético e intelectual de seus profissionais, a Sociedade vem conquistando padrões de excelência e qualidade na prestação de serviços jurídicos, se sustentando em posição de destaque no cenário na Advocacia de Sorocaba e Região. "

```html
<!DOCTYPE html>
<html lang="pt-BR">
<head>
<meta charset="utf-8">
<title>Papel timbrado – Mouralves e Teixedo Sociedade de Advogados</title>
<link rel="stylesheet" href="https://fonts.googleapis.com/css2?family=Cinzel:wght@600&family=Open+Sans:wght@400;600&display=swap">
<style>
  :root{
    --backdrop:#e8e9eb;
    --paper:#ffffff;
    --navy:#1f2f4d;
    --gold:#b9974f;
    --body-text:#8d9299;
    --footer-text:#4b5563;
    --hair:#dcdfe3;
  }
  *{box-sizing:border-box;margin:0;padding:0}
  html,body{width:1200px;height:1200px;overflow:hidden}
  body{background:var(--backdrop);font-family:"Open Sans",Arial,sans-serif;position:relative}
  .letterhead{
    position:absolute;left:204px;top:140px;width:792px;height:1015px;
    background:var(--paper);border:1px solid var(--hair);
    box-shadow:0 4px 18px rgba(0,0,0,.08);
  }
  .brand{position:absolute;top:96px;left:0;width:100%;text-align:center}
  .brand-mark{display:block;width:32px;height:32px;margin:0 auto 12px;background:var(--gold)}
  .brand-name{font-family:"Cinzel",Georgia,serif;font-weight:600;color:var(--navy);
    font-size:22px;letter-spacing:1px;line-height:1.15}
  .brand-sub{font-family:"Cinzel",Georgia,serif;font-weight:600;color:var(--gold);
    font-size:8px;letter-spacing:3.5px;line-height:1.6}
  .brand-web{margin-top:5px;font-size:9.5px;font-weight:600;color:var(--navy);letter-spacing:.6px}
  .body-copy{position:absolute;top:238px;left:70px;width:655px;
    font-size:11.2px;line-height:15px;color:var(--body-text)}
  .body-copy p{margin-bottom:19px}
  .signature{position:absolute;left:600px;top:825px;width:62px;height:28px;
    background:linear-gradient(90deg,rgba(60,70,90,.05),rgba(60,70,90,.2),rgba(60,70,90,.05));border-radius:4px}
  .seal{position:absolute;left:676px;top:820px}
  .footer{position:absolute;left:0;top:934px;width:100%;text-align:center;
    font-size:10px;line-height:1.6;color:var(--footer-text)}
  .footer .label{color:var(--gold);font-weight:600}
</style>
</head>
<body>
  <main class="letterhead">
    <header class="brand">
      <span class="brand-mark"></span>
      <div class="brand-name">MOURALVES E TEIXEDO</div>
      <div class="brand-sub">SOCIEDADE DE ADVOGADOS</div>
      <div class="brand-web">www.mouralvesteixedo.adv.br</div>
    </header>

    <section class="body-copy">
      <p>Lorem ipsum dolor sit amet, consectetur adipiscing elit. In ac magna tellus. Ut pretium faucibus quam, eu porttitor enim condimentum in. Mauris ac erat ac magna pellentesque aliquam. Donec consectetur lectus eget eleifend commodo, augue purus tincidunt tortor, at vulputate urna magna non mauris. Integer nisl quam, mollis quis aliquet non, eleifend molestie dolor. Nulla at dolor nibh. Duis condimentum ornare vehicula. Integer velit nisi, dapibus cursus tincidunt nec, porttitor eu purus.</p>
      <p>Sed sodales commodo eros quis mollis. Duis convallis ante vel urna laoreet ultrices. Fusce eget suscipit massa. Quisque ultrices quam ut nulla porttitor non tempus lectus congue. Praesent id eros ut metus pulvinar sodales vel nec elit. Sed viverra elementum dui, quis faucibus purus tincidunt et. Curabitur felis metus, varius vitae euismod ut, ullamcorper quis justo. Nullam lobortis elit in lectus aliquet ornare. Maecenas euismod placerat est, a auctor neque malesuada ac. Aenean ut orci augue, sed egestas arcu.</p>
      <p>Vestibulum varius vestibulum molestie. Phasellus eu est sed elit ornare facilisis. Nullam ac urna ultricies ante ultrices adipiscing. Fusce nec velit nec arcu placerat tincidunt at id nibh. Suspendisse porttitor arcu eu mauris semper ac molestie dui convallis. Mauris vitae dolor massa, vel tristique nisi. Phasellus in turpis eu lorem suscipit lobortis id ut neque. Duis ac est a tellus egestas lacinia. Aenean scelerisque lacinia diam, vel tincidunt ipsum dignissim sed. Vivamus a ipsum in lacus faucibus placerat a sit amet ipsum.</p>
      <p>Sed sodales commodo eros quis mollis. Duis convallis ante vel urna laoreet ultrices. Fusce eget suscipit massa. Quisque ultrices quam ut nulla porttitor non tempus lectus congue. Praesent id eros ut metus pulvinar sodales vel nec elit. Sed viverra elementum dui, quis faucibus purus tincidunt et. Curabitur felis metus, varius vitae euismod ut, ullamcorper quis justo. Nullam lobortis elit in lectus aliquet ornare. Maecenas euismod placerat est, a auctor neque malesuada ac. Aenean ut orci augue, sed egestas arcu.</p>
      <p>Vestibulum varius vestibulum molestie. Phasellus eu est sed elit ornare facilisis. Nullam ac urna ultricies ante ultrices adipiscing. Fusce nec velit nec arcu placerat tincidunt at id nibh. Suspendisse porttitor arcu eu mauris semper ac molestie dui convallis. Mauris vitae dolor massa, vel tristique nisi. Phasellus in turpis eu lorem suscipit lobortis id ut neque. Duis ac est a tellus egestas lacinia. Aenean scelerisque lacinia diam, vel tincidunt ipsum dignissim sed. Vivamus a ipsum in lacus faucibus placerat a sit amet ipsum.</p>
      <p>Sed sodales commodo eros quis mollis. Duis convallis ante vel urna laoreet ultrices. Fusce eget suscipit massa. Quisque ultrices quam ut nulla porttitor non tempus lectus congue. Praesent id eros ut metus pulvinar sodales vel nec elit. Sed viverra elementum dui, quis faucibus purus tincidunt et. Curabitur felis metus, varius vitae euismod ut, ullamcorper quis justo. Nullam lobortis elit in lectus aliquet ornare. Maecenas euismod placerat est, a auctor neque malesuada ac. Aenean ut orci augue, sed egestas arcu.</p>
    </section>

    <div class="signature" role="img" aria-label="Assinatura manuscrita do sócio responsável"></div>
    <svg class="seal" width="40" height="40" viewBox="0 0 40 40" aria-hidden="true">
      <circle cx="20" cy="20" r="18" fill="none" stroke="#9aa1ab" stroke-width="1.2"/>
    </svg>

    <footer class="footer">
      <div><span class="label">Telefone:</span> + 55 (47) 3200 4417</div>
      <div>Rua Doutor Anselmo Prado, 248 | Jardim Vila Serena</div>
      <div>Vale Dourado/SC | CEP 89470-000</div>
    </footer>
  </main>
</body>
</html>
```